I need a logo design for a new company based in Tucson called "Mindpilot Reg Holloway". I am a psychotherapist that specializes in clinical psychology with athletes and performers. The final design should incorporate the psychology symbol as a watermark. The logo should convey movement and fluidity. "Mindpilot" is a bit of a play on words combining psychology (head) with sports (coach). Other design interests include mid-century, Ansel Brigham Kotter. I will want to use the logo for business cards, letterhead and marketing brochures. I will put together a website at a later date. I am attaching a file with some pertinent information for the business card. Thank you.
Reg Holloway
mindpilotregholloway@quillmarsh.net
Updates

Thank you all for the submissions so far.  I have submitted an additional file with a draft of a new design idea.  Since "mindpilot" is a bit of a play on words, I would like to see something with the two "H's" look something like quotation marks.  If the psychology logo is to be included at all, it needs to be less prominent.     Thank you all.  Reg                               

Target Market(s)

1) Adolescent and adult athletes and performers who are looking to increase their level of performance (Sport and Performance Psychology)
2) Adult psychotherapy patients (Clinical psychology)

Industry/Entity Type

Marketing

Colors

Designer to choose colors to be used in the design.

Requirements
Must have
• 1) Since "mindpilot" is a bit of a play on words, The "H's" need to be in a font that looks somewhat like quotation marks.

Nice to have
• Logo on one side. All other info on the backside?

```html
<!DOCTYPE html>
<html lang="en">
<head>
<meta charset="utf-8">
<title>Mindpilot Reg Holloway – Business Card</title>
<link rel="stylesheet" href="https://fonts.googleapis.com/css2?family=Abril+Fatface&family=Playfair+Display:wght@400&display=swap">
<style>
  :root {
    --card-grey: #8c8c8c;
    --mark-grey: #5f5f5f;
    --mark-grey-soft: #777777;
    --icon-light: #d6d6d6;
    --ink-white: #ffffff;
  }
  html, body {
    margin: 0;
    padding: 0;
    overflow: hidden;
    background: var(--card-grey);
  }
  .card {
    position: relative;
    width: 1200px;
    height: 703px;
    background: var(--card-grey);
    overflow: hidden;
  }
  .watermark-area {
    position: absolute;
    left: 238px;
    top: 44px;
    width: 712px;
    height: 613px;
    border-radius: 40px;
    background: radial-gradient(ellipse at center, var(--mark-grey) 0%, var(--mark-grey-soft) 60%, var(--card-grey) 100%);
    opacity: 0.55;
  }
  .emblem-area {
    position: absolute;
    left: 396px;
    top: 22px;
    width: 302px;
    height: 168px;
    border-radius: 12px;
    background: linear-gradient(90deg, var(--card-grey) 0%, var(--icon-light) 45%, var(--icon-light) 100%);
    opacity: 0.75;
  }
  .brand-name {
    position: absolute;
    left: 0;
    width: 1200px;
    top: 206px;
    margin: 0;
    text-align: center;
    font-family: "Abril Fatface", "Playfair Display", serif;
    font-weight: 400;
    font-size: 68px;
    line-height: 80px;
    color: var(--ink-white);
    letter-spacing: 0.2px;
  }
  .contact-details {
    position: absolute;
    left: 295px;
    top: 292px;
    margin: 0;
    padding: 0;
    list-style: none;
    font-family: "Playfair Display", Georgia, serif;
    font-weight: 400;
    font-size: 29px;
    line-height: 43px;
    color: var(--ink-white);
    font-variant-numeric: oldstyle-nums;
  }
</style>
</head>
<body>
  <main class="card">
    <div class="watermark-area" role="img" aria-label="Large psychology symbol watermark behind the card text"></div>
    <div class="emblem-area" role="img" aria-label="Cyclist icon with speed lines conveying movement"></div>
    <h1 class="brand-name">Mindpilot Reg Holloway</h1>
    <ul class="contact-details">
      <li class="contact-name">Reginald H. Holloway MA</li>
      <li class="contact-title">Licensed Professional Counselor</li>
      <li class="contact-specialty">Clinical &amp; Athletic Performance</li>
      <li class="contact-specialty">Psychology</li>
      <li class="contact-address">4170 East Alder #210 Tucson, AZ 85711</li>
      <li class="contact-phone">520.555.0148 (mobile) 520.555.0172 (fax)</li>
      <li class="contact-email">mindpilotregholloway@quillmarsh.net</li>
    </ul>
  </main>
</body>
</html>
```